Retractable Banners for Corven Talent Alliance

We need to have 2 different retractable banners designed that will be used at a variety of events. We plan to have the banners printed through printmosaic.com. According to their site, specs are as follows:

Retractable banners are digitally printed on 12oz double-sided smooth vinyl. While the area on the retractable banners is 33 x 78, the customer will want to provide a file that has an area of 35 x 82 to account for bleed, with 3" of that vertical bleed at the bottom of the design. Recommended DPI is 150. Upload capacity for Retractable Banners is 100MP.

Banner #1:
Corven Talent Alliance logo at top

Then the following text placed lower on the banner:

Creating Positive Impacts for Lane County Businesses (Heading)

Body of text: Corven Talent Alliance is committed to enhancing the region's ability to meet the workforce needs of local employers through the investments of federal and state funds.

Banner #2:

Meeting the workforce needs of employers and individuals through partnerships and innovation.

You can check out some of our images (water drop, waves) and color schemes we use on our website at corventalent.org.

Target Market(s)

Job seekers, workforce development professionals, city leaders, company CEO's, community members, elected officials.

Industry/Entity Type

Events

Font styles to use
Serif
Sans Serif

Requirements
Must have
• -Be easy to read and understand
• - Must include Corven Talent Alliance logo and text provided for each banner
Nice to have
• color ideas for banners: #0655a3; #0393ce; #00a990; #0355a3; #00a990; #33a6d7
Should not have
• Nothing that depicts gender

```html
<!DOCTYPE html>
<html lang="en">
<head>
<meta charset="utf-8">
<title>Corven Talent Alliance – Retractable Banner</title>
<link rel="stylesheet" href="https://fonts.googleapis.com/css2?family=Montserrat:wght@700&family=Roboto+Condensed:wght@400;700&family=Lato:wght@400&display=swap">
<style>
  :root {
    --page-bg: #e4e4e4;
    --banner-white: #f5f5f5;
    --brand-blue: #0d6fc0;
    --deep-blue: #0655a3;
    --sky-blue: #0393ce;
    --light-blue: #33a6d7;
    --royal-blue: #0a5cbf;
    --ink: #2b2b2b;
    --water-light: #9fb4e6;
    --water-mid: #4e6cb8;
    --water-dark: #0b1430;
  }
  * { margin: 0; padding: 0; box-sizing: border-box; }
  html, body { width: 1200px; height: 1200px; overflow: hidden; }
  body { background: var(--page-bg); position: relative; }

  .banner {
    position: absolute;
    left: 359px; top: 36px;
    width: 482px; height: 1128px;
    background: var(--banner-white);
    overflow: hidden;
  }
  .banner-photo {
    position: absolute; left: 0; top: 0;
    width: 482px; height: 620px;
    background:
      radial-gradient(ellipse 48% 22% at 50% 72%, var(--water-dark) 0%, #1b2a5c 45%, transparent 100%),
      radial-gradient(ellipse 80% 40% at 50% 65%, var(--water-mid) 0%, transparent 90%),
      linear-gradient(180deg, var(--water-light) 0%, #7f98d6 30%, var(--water-mid) 70%, #2a3f80 100%);
  }
  .banner-shapes {
    position: absolute; left: 0; top: 0;
    width: 482px; height: 1128px;
  }
  .brand-name {
    position: absolute; left: 0; top: 728px; width: 482px;
    display: flex; align-items: center; justify-content: center; gap: 12px;
    font-family: "Montserrat", sans-serif; font-weight: 700;
    font-size: 25px; letter-spacing: 0.5px;
    color: var(--brand-blue);
  }
  .brand-mark {
    width: 22px; height: 22px; border-radius: 50%;
    background: var(--brand-blue);
  }
  .headline {
    position: absolute; left: 0; top: 808px; width: 482px;
    text-align: center;
    font-family: "Roboto Condensed", sans-serif;
    text-transform: uppercase;
  }
  .headline-lead {
    display: block; font-weight: 400; font-size: 27px;
    color: var(--ink); line-height: 1.15;
  }
  .headline-focus {
    display: block; font-weight: 700; font-size: 40px;
    color: var(--brand-blue); line-height: 1.1; letter-spacing: -0.3px;
  }
  .mission {
    position: absolute; left: 30px; top: 911px; width: 422px;
    text-align: center;
    font-family: "Lato", sans-serif; font-size: 15.5px; line-height: 1.34;
    color: var(--ink);
  }
</style>
</head>
<body>
  <div class="banner">
    <div class="banner-photo" role="img" aria-label="Close-up photograph of a water drop falling into blue water, sending out rings of ripples"></div>

    <svg class="banner-shapes" viewBox="0 0 602 1410" aria-hidden="true">
      <polygon points="0,735 431,826 602,716 602,1410 0,1410" fill="var(--banner-white)"/>
      <polygon points="0,735 431,826 602,716 602,728 431,842 0,752" fill="#d2d2d2"/>
      <polygon points="0,643 431,742 431,826 0,735" fill="var(--sky-blue)"/>
      <polygon points="60,657 300,712 205,778" fill="var(--light-blue)"/>
      <polygon points="431,742 602,600 602,716 431,826" fill="var(--deep-blue)"/>
      <polygon points="0,1410 0,1375 148,1303 602,1375 602,1410" fill="var(--royal-blue)"/>
      <polygon points="148,1303 602,1375 602,1392 400,1360" fill="#1470d0"/>
    </svg>

    <div class="brand-name"><span class="brand-mark"></span>CORVEN TALENT ALLIANCE</div>

    <h1 class="headline">
      <span class="headline-lead">Creating positive impacts for</span>
      <span class="headline-focus">Lane County Businesses</span>
    </h1>

    <p class="mission">Corven Talent Alliance is committed to enhancing the region's ability to meet the workforce needs of local employers through the investments of federal and state funds.</p>
  </div>
</body>
</html>
```